We need a business card design, letterhead design and envelope design for our corporate image

We are looking for a corporate business card design, letterhead and envelope design to match the business card design. Logo is done.

```html
<!DOCTYPE html>
<html lang="en">
<head>
<meta charset="utf-8">
<title>Vantrel Stationery</title>
<link rel="stylesheet" href="https://fonts.googleapis.com/css2?family=Questrial&family=Open+Sans:wght@400;600&display=swap">
<style>
  :root {
    --backdrop: #c8cbcc;
    --paper: #ffffff;
    --brand-yellow: #f9c80e;
    --brand-gray: #58595b;
    --ink: #2a2a2a;
  }
  * { margin: 0; padding: 0; box-sizing: border-box; }
  html, body { width: 1200px; height: 982px; overflow: hidden; }
  body {
    background: var(--backdrop);
    font-family: "Open Sans", sans-serif;
    position: relative;
  }

  /* Wordmark */
  .wordmark {
    display: flex; align-items: center; gap: 8px;
    font-family: "Questrial", sans-serif;
    color: var(--brand-gray);
    line-height: 1;
    white-space: nowrap;
  }
  .wordmark-square { background: var(--brand-yellow); flex: none; }

  /* Business card */
  .business-card {
    position: absolute; left: 40px; top: 160px;
    width: 320px; height: 183px;
    background: var(--paper);
    box-shadow: 0 6px 14px rgba(0,0,0,.18);
  }
  .card-brand { height: 84px; padding: 24px 0 0 24px; }
  .business-card .wordmark { font-size: 30px; }
  .business-card .wordmark-square { width: 20px; height: 20px; }
  .card-band {
    position: absolute; left: 0; right: 0; bottom: 0; height: 99px;
    background: var(--brand-yellow);
    padding: 14px 20px;
  }
  .card-name { font-family: "Questrial", sans-serif; color: var(--paper); font-size: 16px; }
  .card-title { font-family: "Questrial", sans-serif; color: var(--brand-gray); font-size: 8.5px; letter-spacing: .08em; text-transform: uppercase; margin-top: 3px; }
  .card-contact {
    position: absolute; right: 20px; bottom: 12px;
    text-align: right; font-family: "Questrial", sans-serif;
    color: var(--brand-gray); font-size: 8.5px; line-height: 1.6;
  }

  /* Envelope (long format, upright) */
  .envelope {
    position: absolute; left: 405px; top: 210px;
    width: 220px; height: 460px;
    background: var(--brand-yellow);
    box-shadow: 0 6px 14px rgba(0,0,0,.18);
  }
  .envelope-strip {
    position: absolute; left: 0; top: 0; bottom: 0; width: 72px;
    background: var(--paper);
  }
  .envelope .wordmark {
    position: absolute; left: 16px; bottom: 20px;
    writing-mode: vertical-rl; transform: rotate(180deg);
    font-size: 30px;
  }
  .envelope .wordmark-square { width: 20px; height: 20px; }
  .envelope-return {
    position: absolute; left: 82px; bottom: 20px;
    writing-mode: vertical-rl; transform: rotate(180deg);
    font-family: "Questrial", sans-serif;
    font-size: 9px; line-height: 1.6; color: var(--brand-gray);
  }

  /* Letterhead */
  .letterhead {
    position: absolute; left: 660px; top: 90px;
    width: 500px; height: 647px;
    background: var(--paper);
    box-shadow: 0 6px 16px rgba(0,0,0,.18);
  }
  .letterhead-rules { position: absolute; inset: 0; }
  .letterhead .wordmark { position: absolute; left: 34px; top: 36px; font-size: 34px; }
  .letterhead .wordmark-square { width: 22px; height: 22px; }
  .letter-body {
    position: absolute; left: 50px; top: 150px; width: 380px;
    color: var(--ink); font-size: 10px; line-height: 1.55;
  }
  .salutation { font-size: 16px; font-weight: 600; margin-bottom: 16px; }
  .letter-body p { margin-bottom: 10px; }
  .sign-off { position: absolute; left: 340px; top: 528px; font-size: 10px; color: var(--ink); }
  .signature {
    position: absolute; left: 330px; top: 546px; width: 84px; height: 24px;
    background: linear-gradient(90deg, #e4e4e4, #f2f2f2); border-radius: 4px;
  }
  .letter-footer {
    position: absolute; left: 40px; width: 421px; top: 602px; height: 14px;
    display: flex; align-items: center;
    font-family: "Questrial", sans-serif; font-size: 9px; color: var(--brand-gray);
    white-space: nowrap;
  }
  .footer-rule { height: 0; border-top: 1.5px solid var(--brand-yellow); }
  .footer-rule.lead { width: 36px; margin-right: 8px; }
  .footer-rule.trail { flex: 1; margin-left: 8px; }
  .letter-footer .sep { color: #b5b5b5; margin: 0 5px; }
</style>
</head>
<body>

  <section class="business-card" aria-label="Business card">
    <div class="card-brand">
      <div class="wordmark"><span class="wordmark-square"></span>Vantrel</div>
    </div>
    <div class="card-band">
      <div class="card-name">Jane Doe</div>
      <div class="card-title">Operations Manager</div>
      <div class="card-contact">
        cell: (503) 555-0178<br>
        fax: (503) 555-0143<br>
        jane@vantrel.com
      </div>
    </div>
  </section>

  <section class="envelope" aria-label="Envelope">
    <div class="envelope-strip"></div>
    <div class="wordmark"><span class="wordmark-square"></span>Vantrel</div>
    <div class="envelope-return">
      1234 Address Street<br>
      Portland, Oregon 97206
    </div>
  </section>

  <section class="letterhead" aria-label="Letterhead">
    <svg class="letterhead-rules" width="500" height="647" viewBox="0 0 500 647" aria-hidden="true">
      <polyline points="206,64 460,64 460,609" stroke="#f9c80e" stroke-width="1.5" fill="none"/>
    </svg>

    <div class="wordmark"><span class="wordmark-square"></span>Vantrel</div>

    <div class="letter-body">
      <div class="salutation">Dear Mr. Smith,</div>
      <p>Lorem ipsum dolor sit amet, consectetur adipiscing elit. Donec orci purus, luctus vitae dignissim eu, iaculis sed purus. Vivamus faucibus, ipsum nec aliquet viverra, leo mauris condimentum ligula, sit amet sagittis enim ligula quis arcu. Nam egestas tortor id nisi porttitor mattis. In tortor ante, ultricies in suscipit a, tempus non massa. Vivamus et auctor mi. Fusce vel massa nulla. Phasellus nec eros mauris, et scelerisque orci.</p>
      <p>Donec malesuada orci vitae nulla accumsan porta a id massa. Quisque accumsan iaculis magna sit amet fringilla. Maecenas consequat, magna eget tincidunt semper, odio nibh rutrum mi, id feugiat ante nisi eu risus. Vestibulum nunc orci, rhoncus a placerat in, ultricies in mi. Cras mattis varius eros, vel fringilla nisi suscipit eget. Quisque scelerisque sagittis nulla at porttitor.</p>
      <p>Sed id augue vitae urna euismod commodo aliquet a quam. Pellentesque arcu velit, cursus et malesuada ut, consequat et diam. Nullam erat sem, rhoncus id ullamcorper vitae, rhoncus et arcu. In ultricies ultricies nulla, ut rutrum nisi iaculis at. Donec eu magna a metus ornare faucibus. Fusce aliquet faucibus ultricies. Morbi semper, est id tincidunt gravida, sem arcu adipiscing lacus, ac bibendum nulla leo eu purus. Quisque nec diam sed risus consectetur accumsan quis quis nibh. Vestibulum id purus lorem.</p>
    </div>

    <div class="sign-off">Sincerely,</div>
    <div class="signature" role="img" aria-label="Handwritten signature of John Doe"></div>

    <div class="letter-footer">
      <span class="footer-rule lead"></span>
      <span class="footer-text">503-555-0142<span class="sep">|</span>1234 Address Street<span class="sep">|</span>Portland, OR 97294<span class="sep">|</span>www.vantrel.com</span>
      <span class="footer-rule trail"></span>
    </div>
  </section>

</body>
</html>
```